Kestrel Bridge Consulting (KBC) Business Card Design

I would like to create double-sided business cards that contain:
1) Name: Derek Molvane
2) Phone Number: +1 (555) 218-4907
3) Email: Derek.Molvane@KestrelBridgeConsulting.example
4) Website: KestrelBridgeConsulting.example

I would like to include my logo and a color scheme similar to the Varnholt Grand Prix Ostera squad color scheme (black, silver, greenish-blue – but can also include regular blue)

What we do: Our company develops and delivers innovative and pragmatic information technology and cybersecurity risk and compliance solutions for organizations in the commercial market as well as the federal, and state/local sectors.

```html
<!DOCTYPE html>
<html lang="en">
<head>
<meta charset="utf-8">
<title>Kestrel Bridge Consulting – Business Card</title>
<link rel="stylesheet" href="https://fonts.googleapis.com/css2?family=Michroma&family=Poppins:wght@400&display=swap">
<style>
  :root {
    --backdrop: #2d2d2d;
    --card: #000000;
    --brand-blue: #0b6fb3;
    --brand-teal: #0bcac4;
    --text-light: #ffffff;
    --rule: #bfbfbf;
  }
  * { box-sizing: border-box; margin: 0; padding: 0; }
  html, body { width: 1200px; height: 1015px; overflow: hidden; }
  body { background: var(--backdrop); position: relative; font-family: "Poppins", sans-serif; }

  .card {
    position: absolute;
    width: 640px;
    height: 366px;
    background: var(--card);
    box-shadow: 0 18px 30px rgba(0,0,0,0.45);
  }
  .card--front { left: 110px; top: 100px; }
  .card--back  { left: 450px; top: 545px; }

  /* Front */
  .front-lockup {
    position: absolute;
    left: 50%; top: 50%;
    transform: translate(-50%, -50%);
    display: flex;
    align-items: center;
    gap: 22px;
  }
  .brand-dot {
    width: 62px; height: 62px;
    border-radius: 50%;
    background: var(--brand-teal);
    flex: none;
  }
  .brand-rule { width: 1px; height: 70px; background: var(--rule); flex: none; }
  .brand-name {
    font-family: "Michroma", sans-serif;
    color: var(--text-light);
    font-size: 19px;
    line-height: 1.15;
    letter-spacing: 1px;
    text-transform: uppercase;
  }

  /* Back */
  .back-brand {
    position: absolute;
    right: 46px; top: 38px;
    display: flex;
    align-items: center;
    gap: 16px;
  }
  .back-brand .brand-dot { width: 120px; height: 120px; }
  .back-brand .brand-initials {
    font-family: "Michroma", sans-serif;
    color: var(--brand-teal);
    font-size: 30px;
    letter-spacing: 2px;
  }
  .holder-name {
    position: absolute;
    left: 44px; top: 150px;
    font-family: "Michroma", sans-serif;
    color: var(--brand-blue);
    font-size: 23px;
    letter-spacing: 1px;
    text-transform: uppercase;
  }
  .contact-list {
    position: absolute;
    left: 44px; bottom: 34px;
    list-style: none;
    display: flex;
    flex-direction: column;
    gap: 9px;
  }
  .contact-item {
    display: flex;
    align-items: center;
    gap: 12px;
    color: var(--text-light);
    font-size: 15px;
    letter-spacing: 0.3px;
  }
  .contact-icon { width: 26px; height: 26px; flex: none; }
</style>
</head>
<body>

<section class="card card--front" aria-label="Card front">
  <div class="front-lockup">
    <span class="brand-dot" aria-hidden="true"></span>
    <span class="brand-rule" aria-hidden="true"></span>
    <p class="brand-name">Kestrel Bridge Consulting</p>
  </div>
</section>

<section class="card card--back" aria-label="Card back">
  <div class="back-brand">
    <span class="brand-initials">KBC</span>
    <span class="brand-dot" aria-hidden="true"></span>
  </div>

  <h1 class="holder-name">Derek Molvane</h1>

  <ul class="contact-list">
    <li class="contact-item">
      <svg class="contact-icon" viewBox="0 0 26 26" aria-hidden="true">
        <circle cx="13" cy="13" r="12" fill="none" stroke="var(--brand-blue)" stroke-width="1.5"/>
        <path d="M9 8.5c.6-.6 1.4-.6 1.8 0l1 1.5c.3.5.2 1-.2 1.4l-.6.5c.6 1.3 1.6 2.3 2.9 2.9l.5-.6c.4-.4 1-.5 1.4-.2l1.5 1c.6.4.6 1.2 0 1.8-.9.9-2.2 1.2-3.4.6-2.3-1.1-4.1-2.9-5.2-5.2-.6-1.2-.3-2.5.3-3.7z" fill="var(--brand-teal)"/>
      </svg>
      <span>+1 (555) 218-4907</span>
    </li>
    <li class="contact-item">
      <svg class="contact-icon" viewBox="0 0 26 26" aria-hidden="true">
        <circle cx="13" cy="13" r="12" fill="none" stroke="var(--brand-blue)" stroke-width="1.5"/>
        <rect x="7" y="9" width="12" height="8.5" fill="var(--brand-teal)"/>
        <path d="M7 9l6 5 6-5" fill="none" stroke="#000" stroke-width="1"/>
      </svg>
      <span>Derek.Molvane@KestrelBridgeConsulting.example</span>
    </li>
    <li class="contact-item">
      <svg class="contact-icon" viewBox="0 0 26 26" aria-hidden="true">
        <circle cx="13" cy="13" r="12" fill="none" stroke="var(--brand-blue)" stroke-width="1.5"/>
        <g fill="none" stroke="var(--brand-teal)" stroke-width="1.2">
          <circle cx="13" cy="13" r="6.5"/>
          <ellipse cx="13" cy="13" rx="3" ry="6.5"/>
          <path d="M6.5 13h13M7.5 10h11M7.5 16h11"/>
        </g>
      </svg>
      <span>KestrelBridgeConsulting.example</span>
    </li>
  </ul>
</section>

</body>
</html>
```